Business card for massage therapy company called Brook Fern Wellness

Need business card for massage therapy company called Brook Fern Wellness. Would like my logo on the front and the back of the card I have 3 options of logos and you can play with what looks better.

Would like this information displayed on the back of the card:

Marcus Ellery
Licensed Massage Therapist
321-555-0147
brookfern-example.com
brookfern_rest_

```html
<!DOCTYPE html>
<html lang="en">
<head>
<meta charset="utf-8">
<title>Brook Fern Wellness – Business Card</title>
<link href="https://fonts.googleapis.com/css2?family=Montserrat:wght@400;500;800&display=swap" rel="stylesheet">
<style>
  :root {
    --backdrop: #2f2f31;
    --olive: #5c6641;
    --olive-light: #6a7449;
    --sage-text: #6b7258;
    --ink: #3a3a3a;
    --accent: #c8733a;
    --paper: #ffffff;
    --divider: #8a8f7a;
  }
  * { margin: 0; padding: 0; box-sizing: border-box; }
  html, body {
    width: 1200px; height: 758px; overflow: hidden;
    background: var(--backdrop);
    font-family: "Montserrat", sans-serif;
  }
  .canvas {
    position: relative; width: 1200px; height: 758px;
    display: flex; align-items: center; justify-content: center; gap: 40px;
  }
  .card {
    position: relative; width: 540px; height: 309px;
    border-radius: 18px; overflow: hidden;
  }
  .card--front { background: var(--olive); }
  .monogram-pattern {
    position: absolute; inset: 0;
    background: linear-gradient(120deg, var(--olive-light) 0%, var(--olive) 55%, #535c3a 100%);
  }
  .front-brand {
    position: absolute; right: 46px; top: 50%; transform: translateY(-50%);
    display: flex; align-items: center; gap: 12px;
    color: var(--paper);
  }
  .front-brand__circle {
    width: 38px; height: 38px; border: 2px solid var(--paper); border-radius: 50%;
  }
  .front-brand__name {
    font-size: 20px; font-weight: 400; letter-spacing: 0.14em; text-transform: uppercase;
  }
  .card--back { background: var(--paper); display: flex; align-items: center; }
  .back-brand {
    width: 250px; padding-left: 34px;
    font-size: 30px; font-weight: 400; line-height: 1.15; color: var(--sage-text);
  }
  .divider {
    width: 1px; height: 150px; background: var(--divider); margin: 0 26px 0 6px;
  }
  .details { color: var(--ink); }
  .details__name {
    font-size: 25px; font-weight: 800; color: var(--sage-text); line-height: 1.1;
  }
  .details__title { font-size: 13.5px; font-weight: 400; margin-top: 4px; }
  .contact { list-style: none; margin-top: 18px; }
  .contact__item {
    display: flex; align-items: center; gap: 8px;
    font-size: 14px; font-weight: 500; line-height: 1.65;
  }
  .contact__icon { width: 13px; height: 13px; flex: none; }
</style>
</head>
<body>
<main class="canvas">
  <section class="card card--front" aria-label="Card front">
    <div class="monogram-pattern" role="img" aria-label="Repeating embossed brand monogram pattern in olive tones"></div>
    <div class="front-brand">
      <span class="front-brand__circle"></span>
      <span class="front-brand__name">Brook Fern Wellness</span>
    </div>
  </section>

  <section class="card card--back" aria-label="Card back">
    <div class="back-brand">Brook Fern Wellness</div>
    <div class="divider"></div>
    <div class="details">
      <h1 class="details__name">Marcus Ellery</h1>
      <p class="details__title">Licensed Massage Therapist</p>
      <ul class="contact">
        <li class="contact__item">
          <svg class="contact__icon" viewBox="0 0 24 24" aria-hidden="true"><path fill="var(--accent)" d="M6.6 10.8a15.1 15.1 0 0 0 6.6 6.6l2.2-2.2a1 1 0 0 1 1-.25 11.4 11.4 0 0 0 3.6.57 1 1 0 0 1 1 1V20a1 1 0 0 1-1 1A17 17 0 0 1 3 4a1 1 0 0 1 1-1h3.5a1 1 0 0 1 1 1c0 1.25.2 2.45.57 3.57a1 1 0 0 1-.25 1z"/></svg>
          321-555-0147
        </li>
        <li class="contact__item">
          <svg class="contact__icon" viewBox="0 0 24 24" aria-hidden="true" fill="none" stroke="var(--accent)" stroke-width="2"><circle cx="12" cy="12" r="10"/><path d="M2 12h20M12 2c3 3 3 17 0 20M12 2c-3 3-3 17 0 20"/></svg>
          brookfern-example.com
        </li>
        <li class="contact__item">
          <svg class="contact__icon" viewBox="0 0 24 24" aria-hidden="true"><circle cx="12" cy="12" r="9" fill="none" stroke="var(--accent)" stroke-width="2.5"/></svg>
          brookfern_rest_
        </li>
      </ul>
    </div>
  </section>
</main>
</body>
</html>
```